Velmo und Korvex Smartphone Reparatur - PPC - Affiliate
Zielgruppe
Wir gründen ein Unternehmen, welches sich ausschließlich mit hochwertigen Reparaturen von Velmos und Korvex Smartphones beschäftigt. Wir bieten Reparaturen innerhalb 48 Stunden, hochwertige Ersatzteile und die Abholung des Gerätes von zu Hause an. Einen Slogan haben wir noch nicht.
Aufgabenstellung
Da wir ein Unternehmen im Bereich Technologie gründen, ist es wichtig für uns, dass man "Technik" sieht. Die Banner sollten deshalb auf jedenfall modern sein und möglichst das Orange/Weiß oder Orange/Schwarz der Startseite unserer Website beinhalten.
Die größen der Banner:
250 x 250
200 x 200
468 x 60
728 x 90
300 x 250
120 x 600
160 x 600
Einen Slogan haben wir noch nicht.
Sollten Sie für die Banner etwas von unserer Website benötigen, dürfen Sie sich gerne bedienen.
www.lunqor.de

```html
<!DOCTYPE html>
<html lang="de">
<head>
<meta charset="utf-8">
<title>Lunqor Smartphone Reparatur – Banner 300x250</title>
<link href="https://fonts.googleapis.com/css2?family=PT+Sans:wght@400;700&display=swap" rel="stylesheet">
<style>
  :root {
    --page-top: #ffffff;
    --page-mid: #ececec;
    --page-bottom: #c9c9c9;
    --label: #3a3a3a;
    --white: #ffffff;
    --ink: #111111;
    --orange: #f5a031;
    --footer: #111111;
    --photo-a: #eef1f0;
    --photo-b: #c9ccc6;
    --photo-c: #b6d98a;
  }
  * { margin: 0; padding: 0; box-sizing: border-box; }
  html, body { width: 1041px; height: 1200px; overflow: hidden; }
  body {
    position: relative;
    font-family: "PT Sans", sans-serif;
    background: linear-gradient(180deg, var(--page-top) 0%, var(--page-mid) 55%, var(--page-bottom) 100%);
  }
  .size-label {
    position: absolute;
    top: 180px; left: 0; width: 100%;
    text-align: center;
    font-weight: 700;
    font-size: 33px;
    letter-spacing: 1px;
    color: var(--label);
  }
  .banner {
    position: absolute;
    left: 221px; top: 300px;
    width: 626px; height: 521px;
    background: var(--white);
    box-shadow: 0 6px 30px rgba(0,0,0,0.18);
    overflow: hidden;
  }
  .brand-bar {
    height: 104px;
    display: flex; align-items: center; justify-content: center; gap: 16px;
  }
  .brand-mark { width: 54px; height: 54px; }
  .brand-name { font-weight: 700; font-size: 50px; letter-spacing: 4px; color: var(--ink); }
  .brand-tagline { font-size: 17px; line-height: 1.05; color: var(--ink); font-weight: 700; }
  .hero {
    position: absolute; left: 0; top: 104px;
    width: 626px; height: 363px;
    background:
      radial-gradient(ellipse 40% 55% at 72% 50%, var(--photo-c) 0%, rgba(182,217,138,0) 70%),
      radial-gradient(ellipse 50% 60% at 20% 40%, var(--photo-b) 0%, rgba(201,204,198,0) 75%),
      var(--photo-a);
  }
  .headline-box {
    position: absolute; left: 73px; top: 107px;
    width: 476px; height: 92px;
    background: rgba(255,255,255,0.82);
    border: 2px solid var(--white);
    outline: 1px solid rgba(0,0,0,0.15);
    display: flex; align-items: center; justify-content: center;
  }
  .headline { font-weight: 700; font-size: 38px; color: var(--ink); }
  .cta {
    position: absolute; left: 138px; top: 382px;
    width: 361px; height: 69px;
    background: var(--orange);
    border-radius: 4px;
    display: flex; align-items: center; justify-content: center;
    color: var(--white); font-weight: 700; font-size: 40px; letter-spacing: 1px;
  }
  .footer {
    position: absolute; left: 0; bottom: 0;
    width: 626px; height: 54px;
    background: var(--footer);
    display: flex; align-items: center; justify-content: center;
    color: var(--white); font-weight: 700; font-size: 34px;
  }
</style>
</head>
<body>
  <div class="size-label">300X250</div>
  <div class="banner">
    <div class="brand-bar">
      <svg class="brand-mark" viewBox="0 0 54 54" aria-hidden="true"><circle cx="27" cy="27" r="26" fill="var(--ink)"/></svg>
      <span class="brand-name">LUNQOR</span>
      <span class="brand-tagline">Smartphone<br>Reparatur</span>
    </div>
    <div class="hero" role="img" aria-label="Foto: Hände in Handschuhen reparieren ein geöffnetes Smartphone mit grünem Gehäuse"></div>
    <div class="headline-box"><span class="headline">Schnell Und Professionell</span></div>
    <div class="cta">KLICKEN HIER</div>
    <div class="footer">www.lunqor.de</div>
  </div>
</body>
</html>
```